Postcard Design

Dentist Office trying to attract new patients
11" x 6" Print Size ("Postcard template" on brief is not required)

Target Market(s)

Moms with kids, Families, Everybody

Industry/Entity Type

Office

Requirements
Must have
• Postage requirements or template are not required in this project. Please use the following guidelines instead.

(11" x 6") Print Size
Requirements for QTRV Retail Indicia (attached file)
* Place the QTRV Retail Indicia in the upper right hand corner of the mail piece.
* Leave 1/8" space from top and right edge.
* Should fit in the area 1.625" from the right edge and 1.375" from top edge.
* No specific size requirement, but must be larger than .5" x .5".
* Font must be in all caps and minimum 4 point size.

The design should focus on quality, comfort and convenience of a dental office. check out the website www.lowvaleteeth.com for ideas.
Include:
-Accepting most PPO Insurance plans
-Evening and Saturday appointments available
- New Patient Specials ...
*Using the logo is optional.

```html
<!DOCTYPE html>
<html lang="en">
<head>
<meta charset="utf-8">
<title>Lowvale Family and Cosmetic Dentistry – Postcard</title>
<link rel="stylesheet" href="https://fonts.googleapis.com/css2?family=Noto+Serif:ital,wght@0,400;1,400&family=Italianno&display=swap">
<style>
  :root {
    --sky: #1bb6ee;
    --sky-light: #45c8f4;
    --sky-deep: #0fa3dc;
    --white: #ffffff;
    --band: rgba(255, 255, 255, 0.6);
    --quote-light: rgba(255, 255, 255, 0.42);
    --quote-dark: rgba(58, 74, 82, 0.62);
    --photo-light: #e6e4e1;
    --photo-mid: #b9b2ab;
    --photo-skin: #e7b49c;
    --photo-teal: #9fc6cc;
  }
  html, body {
    margin: 0;
    padding: 0;
    width: 1200px;
    height: 655px;
    overflow: hidden;
    background: #ffffff;
  }
  .postcard {
    position: relative;
    width: 1200px;
    height: 655px;
    overflow: hidden;
    font-family: "Noto Serif", Georgia, serif;
  }
  .patient-photo {
    position: absolute;
    inset: 0;
    background:
      radial-gradient(ellipse 260px 300px at 250px 330px, var(--photo-skin) 0%, rgba(231,180,156,0.6) 55%, rgba(231,180,156,0) 100%),
      radial-gradient(ellipse 320px 200px at 160px 620px, var(--photo-teal) 0%, rgba(159,198,204,0) 100%),
      radial-gradient(ellipse 260px 220px at 620px 520px, #6f7b80 0%, rgba(111,123,128,0) 100%),
      linear-gradient(100deg, #3a3330 0%, var(--photo-mid) 30%, var(--photo-light) 60%, #f2f2f2 100%);
  }
  .wave-panel {
    position: absolute;
    inset: 0;
  }
  .indicia {
    position: absolute;
    right: 14px;
    top: 14px;
    width: 72px;
    height: 60px;
    box-sizing: border-box;
    border: 1.5px solid var(--white);
    display: flex;
    flex-direction: column;
    align-items: center;
    justify-content: center;
    color: var(--white);
    font-size: 8px;
    line-height: 11px;
    letter-spacing: 0.3px;
    text-transform: uppercase;
    text-align: center;
  }
  .practice-name {
    position: absolute;
    right: 26px;
    top: 80px;
    margin: 0;
    color: var(--white);
    font-weight: 400;
    font-style: italic;
    text-align: right;
    white-space: nowrap;
  }
  .practice-name .line-one {
    display: block;
    font-size: 40px;
    line-height: 46px;
  }
  .practice-name .line-two {
    display: block;
    font-size: 28px;
    line-height: 42px;
  }
  .welcome-quote {
    position: absolute;
    left: 462px;
    top: 230px;
    width: 308px;
    height: 290px;
    box-sizing: border-box;
    padding: 10px 12px 0 12px;
    margin: 0;
    background: linear-gradient(to bottom,
      var(--quote-light) 0px, var(--quote-light) 138px,
      var(--quote-dark) 170px, var(--quote-dark) 290px);
    font-style: italic;
    font-size: 19.5px;
    line-height: 33.5px;
    letter-spacing: 0.5px;
    color: var(--sky);
    white-space: nowrap;
  }
  .welcome-quote .on-dark { color: var(--white); }
  .benefits {
    list-style: none;
    margin: 0;
    padding: 0;
  }
  .benefit {
    position: absolute;
    color: var(--white);
    font-style: italic;
    font-size: 29px;
    line-height: 34px;
    white-space: nowrap;
  }
  .benefit::before {
    content: "";
    position: absolute;
    left: -36px;
    top: 28px;
    width: 14px;
    height: 14px;
    border-radius: 50%;
    background: var(--white);
  }
  .benefit-hours { left: 822px; top: 252px; }
  .benefit-insurance { left: 861px; top: 366px; }
  .benefit-specials { left: 900px; top: 466px; }
  .benefit-specials::before { top: 11px; }
  .contact {
    position: absolute;
    display: flex;
    align-items: center;
    gap: 10px;
    color: var(--white);
    font-size: 15.5px;
    white-space: nowrap;
  }
  .contact-email { left: 917px; top: 543px; }
  .contact-phone { left: 1022px; top: 598px; }
  .contact-icon {
    width: 30px;
    height: 30px;
    border-radius: 50%;
    background: var(--white);
    display: flex;
    align-items: center;
    justify-content: center;
    color: var(--sky);
    font-size: 18px;
  }
  .tagline-band {
    position: absolute;
    left: 0;
    top: 576px;
    width: 650px;
    height: 79px;
    background: var(--band);
  }
  .tagline {
    position: absolute;
    left: 26px;
    top: 570px;
    margin: 0;
    font-family: "Italianno", cursive;
    font-weight: 400;
    font-size: 80px;
    line-height: 84px;
    color: var(--sky);
    white-space: nowrap;
  }
</style>
</head>
<body>
<div class="postcard">
  <div class="patient-photo" role="img" aria-label="Photo of a smiling young woman with dark braided hair seated in a dental chair"></div>

  <svg class="wave-panel" width="1200" height="655" viewBox="0 0 1200 655" aria-hidden="true">
    <defs>
      <linearGradient id="panelFill" x1="0" y1="0" x2="1" y2="1">
        <stop offset="0" stop-color="#45c8f4"/>
        <stop offset="0.6" stop-color="#1bb6ee"/>
        <stop offset="1" stop-color="#12a8e2"/>
      </linearGradient>
    </defs>
    <path d="M545 0 C 620 110, 690 250, 750 370 C 800 470, 850 560, 905 655 L 1200 655 L 1200 0 Z" fill="url(#panelFill)"/>
    <path d="M690 170 C 820 240, 960 180, 1200 175" fill="none" stroke="#ffffff" stroke-opacity="0.45" stroke-width="1.5"/>
    <path d="M800 440 C 900 430, 1020 470, 1200 520" fill="none" stroke="#ffffff" stroke-opacity="0.45" stroke-width="1.5"/>
  </svg>

  <div class="indicia"><span>PRSRT STD</span><span>US POSTAGE</span><span>PAID</span><span>QTRV</span></div>

  <h1 class="practice-name"><span class="line-one">Lowvale Family</span><span class="line-two">and Cosmetic Dentistry</span></h1>

  <p class="welcome-quote">“When you visit our<br>office you will know<br>from the moment you<br>walk in that we take<br>pride in <span class="on-dark">providing you<br>with exceptional patient<br>care in a comfortable<br>caring environment.”</span></p>

  <ul class="benefits">
    <li class="benefit benefit-hours">Evening and Saturday<br>appointments available</li>
    <li class="benefit benefit-insurance">Accepting most PPO<br>Insurance plans</li>
    <li class="benefit benefit-specials">New Patient Specials</li>
  </ul>

  <div class="contact contact-email"><span class="contact-icon">@</span><span>lowvaledentistry@gmail.com</span></div>
  <div class="contact contact-phone">
    <span class="contact-icon">
      <svg width="16" height="16" viewBox="0 0 24 24" aria-hidden="true"><path fill="#1bb6ee" d="M6.6 10.8a15.1 15.1 0 0 0 6.6 6.6l2.2-2.2a1 1 0 0 1 1-.25 11.4 11.4 0 0 0 3.6.57 1 1 0 0 1 1 1V20a1 1 0 0 1-1 1A17 17 0 0 1 3 4a1 1 0 0 1 1-1h3.5a1 1 0 0 1 1 1c0 1.25.2 2.45.57 3.57a1 1 0 0 1-.25 1z"/></svg>
    </span>
    <span>(555) 014-2297</span>
  </div>

  <div class="tagline-band"></div>
  <p class="tagline">We want to see you smile :)</p>
</div>
</body>
</html>
```